Design mobile friendly review and ranking site

We're working on a corporate website for reviewing and ranking fellow employees. We need the website to look both fun and professional and it needs to be responsive - to it works on mobile and desktop.

Looking for css and HTML for 3 key pages as well as a header and footer for the site. Also would need any supporting graphics as part of the design.

Target Market(s)

Professionals in their 20s, 30s, and 40s.

Industry/Entity Type

Internet

Coding

Coded - Design and coding required

Number of Pages Required

3 page

Font styles to use
Sans Serif

Requirements
Must have
• 3 key pages we need (note included screenshots for each - these are just super rough cuts so you see examples of the content.)
• a) main-intro: A compelling into page with a login/registration form. Should be sleek/modern/enticing. Also we would show the ranking for the top 3 people to tease people re: content.
• b) main-page: Has two sections: One at the top where you would rate someone and one at the bottom where it shows a ranking of people.
• c) profile page: This is where you view a specific person. You see the person's picture, some info about the person, you see their overall rating, you can rate them, and you also see their historical ratings.
Nice to have
• Note we need css and HTML for this. It should feel as sleek and modern. Note also must be responsive design so it works well in mobile and desktop.

```html
<!DOCTYPE html>
<html lang="en">
<head>
<meta charset="utf-8">
<title>Prime Desk Rankings</title>
<link rel="stylesheet" href="https://fonts.googleapis.com/css2?family=Raleway:ital,wght@0,400;0,500;0,600;0,700;1,400&family=Lato:wght@400;700&display=swap">
<style>
:root{
  --header-bg:#eef3f6;
  --ink:#1f2326;
  --white:#ffffff;
  --dark-btn:#2b2b2d;
  --purple:#6a2fa3;
  --purple-border:#8a52c6;
  --panel:rgba(40,60,95,.45);
  --panel-head:rgba(70,70,90,.55);
  --panel-deep:rgba(25,40,110,.45);
  --select:rgba(150,175,195,.55);
  --rule:rgba(255,255,255,.35);
  --muted:rgba(210,225,240,.75);
  --star-on:#f7c000;
  --star-off:#6a5a5c;
  --footer:#050507;
}
*{box-sizing:border-box;margin:0;padding:0}
html,body{width:1192px;height:1200px;overflow:hidden}
body{position:relative;font-family:'Lato',sans-serif;color:var(--white);
  background:linear-gradient(135deg,#52c8d8 0%,#2f9fcb 28%,#2a6fbf 50%,#2c3fa6 72%,#2a138a 100%)}
.site-header{position:absolute;left:0;top:0;width:1192px;height:82px;background:var(--header-bg);box-shadow:0 2px 4px rgba(0,0,0,.25)}
.brand{position:absolute;left:55px;top:19px;font-family:'Raleway',sans-serif;font-weight:600;font-size:37px;letter-spacing:2px;color:var(--ink);text-transform:uppercase}
.header-actions{position:absolute;right:52px;top:23px;display:flex;gap:10px}
.hbtn{height:35px;display:flex;align-items:center;gap:6px;padding:0 9px;font-family:'Lato',sans-serif;font-weight:700;font-size:15px;color:var(--white);border-radius:2px}
.hbtn.profile{background:var(--dark-btn);border:1px solid #111;width:121px}
.hbtn.logout{background:var(--purple);border:1px solid var(--purple-border);width:93px}
.hbtn svg{width:20px;height:20px;fill:var(--white)}

.rate-panel{position:absolute;left:51px;top:114px;width:1089px;height:372px;background:var(--panel);border-radius:6px;overflow:hidden}
.rate-title{height:65px;background:var(--panel-head);font-family:'Raleway',sans-serif;font-size:28px;letter-spacing:1px;text-align:center;line-height:68px;text-transform:uppercase}
.portrait-frame{position:absolute;border:1px solid rgba(255,255,255,.85);padding:6px}
.portrait-frame.large{left:27px;top:95px;width:200px;height:223px}
.portrait{position:relative;width:100%;height:100%;background:linear-gradient(160deg,#a9adb4,#6f7379 55%,#3a3d44)}
.portrait-caption{position:absolute;left:0;bottom:0;width:100%;height:30px;background:rgba(40,40,45,.7);text-align:center;font-family:'Raleway',sans-serif;font-weight:600;font-size:15px;line-height:30px}
.person-head{position:absolute;left:247px;top:96px;display:flex;align-items:baseline}
.person-name{font-family:'Raleway',sans-serif;font-size:35px;font-weight:400;text-transform:uppercase}
.review-count{font-family:'Raleway',sans-serif;font-style:italic;font-size:16px;color:var(--muted);margin-left:14px;padding-left:14px;border-left:1px solid var(--muted);line-height:16px}
.traits{position:absolute;list-style:none}
.traits li{display:flex;justify-content:space-between;align-items:center;border-top:1px dotted rgba(255,255,255,.4)}
.traits li:last-child{border-bottom:1px dotted rgba(255,255,255,.4)}
.traits.large{left:247px;top:142px;width:363px}
.traits.large li{height:42px;padding:0 12px 0 4px;font-family:'Raleway',sans-serif;font-weight:700;font-size:17px}
.stars{display:block}
.btn{position:absolute;display:flex;align-items:center;justify-content:center;font-family:'Raleway',sans-serif;font-size:16px;color:var(--white);text-transform:uppercase;border-radius:3px}
.btn.dark{background:var(--dark-btn);border:1px solid #111}
.btn.purple{background:var(--purple);border:1px solid var(--purple-border)}
.view-reviews{left:250px;top:284px;width:177px;height:39px}
.rate-label{position:absolute;left:648px;top:109px;display:flex;align-items:center;gap:14px;font-weight:700;font-size:15px}
.comment-box{position:absolute;left:652px;top:136px;width:410px;height:126px;background:var(--white);border-radius:4px;padding:10px 14px;font-weight:700;font-size:15px;color:var(--ink)}
.skip{left:652px;top:284px;width:93px;height:35px}
.save{left:757px;top:284px;width:93px;height:35px}

.search-bar{position:absolute;left:51px;top:515px;width:1089px;height:74px;background:rgba(30,45,90,.45);border-radius:6px}
.select{position:absolute;top:16px;height:42px;background:var(--select);border-radius:3px;padding:0 15px;display:flex;align-items:center;justify-content:space-between;font-family:'Raleway',sans-serif;font-weight:700;font-size:17px}
.select svg{width:16px;height:10px;fill:none;stroke:var(--white);stroke-width:1.5}
.sel-best{left:23px;width:205px}
.sel-func{left:270px;width:307px}
.sel-level{left:644px;width:307px}
.joiner{position:absolute;top:22px;font-family:'Raleway',sans-serif;font-size:22px}
.join-in{left:240px}
.join-and{left:592px}
.search-btn{left:967px;top:16px;width:102px;height:42px}

.ranking-panel{position:absolute;left:51px;top:603px;width:1089px;height:517px;background:var(--panel-deep)}
.rank-card{position:absolute;width:490px;height:203px;border-bottom:1px solid rgba(255,255,255,.85)}
.rc1{left:35px;top:46px}.rc2{left:567px;top:46px}
.rc3{left:35px;top:289px}.rc4{left:567px;top:289px}
.portrait-frame.small{left:0;top:0;width:158px;height:158px;padding:4px}
.portrait.small{background:linear-gradient(150deg,#d9dcd6,#a2948a 45%,#4a4a4c)}
.rank-badge{position:absolute;left:0;top:0;width:72px;height:72px;background:var(--purple);clip-path:polygon(0 0,100% 0,0 100%)}
.rank-num{position:absolute;left:8px;top:3px;font-size:17px}
.rank-num sup{font-size:10px}
.rank-tag{position:absolute;left:5px;top:30px;font-size:11px}
.card-name{position:absolute;left:190px;top:-2px;font-family:'Raleway',sans-serif;font-size:25px;text-transform:uppercase}
.card-count{position:absolute;left:191px;top:31px;font-family:'Raleway',sans-serif;font-style:italic;font-size:14px;color:var(--muted)}
.traits.small{left:190px;top:61px;width:300px}
.traits.small li{height:31px;padding:0 10px 0 3px;font-family:'Raleway',sans-serif;font-weight:700;font-size:14px}
.traits.small li:first-child{border-top:1px solid rgba(255,255,255,.3)}
.view-details{left:369px;top:170px;width:121px;height:33px;font-size:14px;border-radius:0;border:1px solid rgba(255,255,255,.85)!important}

.site-footer{position:absolute;left:0;top:1153px;width:1192px;height:47px;background:var(--footer);text-align:center;line-height:47px;font-size:15px}
.on{fill:var(--star-on)}.off{fill:var(--star-off)}
</style>
</head>
<body>
<svg width="0" height="0" style="position:absolute">
  <defs>
    <symbol id="star" viewBox="0 0 24 24"><path d="M12 1.5l3.2 6.9 7.5.8-5.6 5.1 1.6 7.4L12 17.9l-6.7 3.8 1.6-7.4L1.3 9.2l7.5-.8z"/></symbol>
  </defs>
</svg>

<header class="site-header">
  <div class="brand">Prime Desk Rankings</div>
  <nav class="header-actions">
    <a class="hbtn profile"><svg viewBox="0 0 24 24"><circle cx="12" cy="7" r="5"/><path d="M2 22c0-6 4.5-9 10-9s10 3 10 9z"/></svg>Your Profile</a>
    <a class="hbtn logout"><svg viewBox="0 0 24 24"><path d="M3 3h11v4h-2V5H5v14h7v-2h2v4H3z"/><path d="M14 8l6 4-6 4v-3H8v-2h6z"/></svg>Logout</a>
  </nav>
</header>

<section class="rate-panel">
  <h1 class="rate-title">Anonymously rate this person for a point</h1>
  <div class="portrait-frame large">
    <div class="portrait" role="img" aria-label="Portrait photo of Daniel">
      <div class="portrait-caption">DANIEL</div>
    </div>
  </div>
  <div class="person-head"><span class="person-name">Daniel</span><span class="review-count">Number Of Reviews : 45</span></div>
  <ul class="traits large">
    <li>Smart<svg class="stars" width="120" height="22" viewBox="0 0 120 22"><use href="#star" x="0" width="22" height="22" class="on"/><use href="#star" x="25" width="22" height="22" class="on"/><use href="#star" x="50" width="22" height="22" class="on"/><use href="#star" x="75" width="22" height="22" class="on"/><use href="#star" x="100" width="22" height="22" class="off"/></svg></li>
    <li>Average Personality<svg class="stars" width="120" height="22" viewBox="0 0 120 22"><use href="#star" x="0" width="22" height="22" class="on"/><use href="#star" x="25" width="22" height="22" class="on"/><use href="#star" x="50" width="22" height="22" class="on"/><use href="#star" x="75" width="22" height="22" class="off"/><use href="#star" x="100" width="22" height="22" class="off"/></svg></li>
    <li>Works Crazy Hard<svg class="stars" width="120" height="22" viewBox="0 0 120 22"><use href="#star" x="0" width="22" height="22" class="on"/><use href="#star" x="25" width="22" height="22" class="on"/><use href="#star" x="50" width="22" height="22" class="on"/><use href="#star" x="75" width="22" height="22" class="on"/><use href="#star" x="100" width="22" height="22" class="on"/></svg></li>
  </ul>
  <a class="btn dark view-reviews">View Reviews</a>
  <div class="rate-label">Rate Him:<svg class="stars" width="120" height="22" viewBox="0 0 120 22"><use href="#star" x="0" width="22" height="22" class="on"/><use href="#star" x="25" width="22" height="22" class="on"/><use href="#star" x="50" width="22" height="22" class="on"/><use href="#star" x="75" width="22" height="22" class="on"/><use href="#star" x="100" width="22" height="22" class="off"/></svg></div>
  <div class="comment-box">Comment</div>
  <a class="btn dark skip">Skip</a>
  <a class="btn purple save">Save</a>
</section>

<form class="search-bar">
  <div class="select sel-best">Best<svg viewBox="0 0 16 10"><path d="M1 1l7 7 7-7"/></svg></div>
  <span class="joiner join-in">in</span>
  <div class="select sel-func">All Functions<svg viewBox="0 0 16 10"><path d="M1 1l7 7 7-7"/></svg></div>
  <span class="joiner join-and">and</span>
  <div class="select sel-level">All Levels<svg viewBox="0 0 16 10"><path d="M1 1l7 7 7-7"/></svg></div>
  <a class="btn purple search-btn">Search</a>
</form>

<section class="ranking-panel">
  <article class="rank-card rc1">
    <div class="portrait-frame small"><div class="portrait small" role="img" aria-label="Portrait photo of Sam Turner" style="position:relative;width:100%;height:100%"><div class="rank-badge"></div><span class="rank-num">1<sup>st</sup></span><span class="rank-tag">BEST</span></div></div>
    <h2 class="card-name">Sam Turner</h2><p class="card-count">Number Of Reviews : 45</p>
    <ul class="traits small">
      <li>Smart<svg width="86" height="14" viewBox="0 0 86 14"><use href="#star" x="0" width="14" height="14" class="on"/><use href="#star" x="18" width="14" height="14" class="on"/><use href="#star" x="36" width="14" height="14" class="on"/><use href="#star" x="54" width="14" height="14" class="on"/><use href="#star" x="72" width="14" height="14" class="off"/></svg></li>
      <li>Average Personality<svg width="86" height="14" viewBox="0 0 86 14"><use href="#star" x="0" width="14" height="14" class="on"/><use href="#star" x="18" width="14" height="14" class="on"/><use href="#star" x="36" width="14" height="14" class="on"/><use href="#star" x="54" width="14" height="14" class="off"/><use href="#star" x="72" width="14" height="14" class="off"/></svg></li>
      <li>Works Crazy Hard<svg width="86" height="14" viewBox="0 0 86 14"><use href="#star" x="0" width="14" height="14" class="on"/><use href="#star" x="18" width="14" height="14" class="on"/><use href="#star" x="36" width="14" height="14" class="on"/><use href="#star" x="54" width="14" height="14" class="on"/><use href="#star" x="72" width="14" height="14" class="on"/></svg></li>
    </ul>
    <a class="btn dark view-details">View Details</a>
  </article>
  <article class="rank-card rc2">
    <div class="portrait-frame small"><div class="portrait small" role="img" aria-label="Portrait photo of Sam Turner" style="position:relative;width:100%;height:100%"><div class="rank-badge"></div><span class="rank-num">2<sup>st</sup></span><span class="rank-tag">BEST</span></div></div>
    <h2 class="card-name">Sam Turner</h2><p class="card-count">Number Of Reviews : 45</p>
    <ul class="traits small">
      <li>Smart<svg width="86" height="14" viewBox="0 0 86 14"><use href="#star" x="0" width="14" height="14" class="on"/><use href="#star" x="18" width="14" height="14" class="on"/><use href="#star" x="36" width="14" height="14" class="on"/><use href="#star" x="54" width="14" height="14" class="on"/><use href="#star" x="72" width="14" height="14" class="off"/></svg></li>
      <li>Average Personality<svg width="86" height="14" viewBox="0 0 86 14"><use href="#star" x="0" width="14" height="14" class="on"/><use href="#star" x="18" width="14" height="14" class="on"/><use href="#star" x="36" width="14" height="14" class="on"/><use href="#star" x="54" width="14" height="14" class="off"/><use href="#star" x="72" width="14" height="14" class="off"/></svg></li>
      <li>Works Crazy Hard<svg width="86" height="14" viewBox="0 0 86 14"><use href="#star" x="0" width="14" height="14" class="on"/><use href="#star" x="18" width="14" height="14" class="on"/><use href="#star" x="36" width="14" height="14" class="on"/><use href="#star" x="54" width="14" height="14" class="on"/><use href="#star" x="72" width="14" height="14" class="on"/></svg></li>
    </ul>
    <a class="btn dark view-details">View Details</a>
  </article>
  <article class="rank-card rc3">
    <div class="portrait-frame small"><div class="portrait small" role="img" aria-label="Portrait photo of Sam Turner" style="position:relative;width:100%;height:100%"><div class="rank-badge"></div><span class="rank-num">3<sup>st</sup></span><span class="rank-tag">BEST</span></div></div>
    <h2 class="card-name">Sam Turner</h2><p class="card-count">Number Of Reviews : 45</p>
    <ul class="traits small">
      <li>Smart<svg width="86" height="14" viewBox="0 0 86 14"><use href="#star" x="0" width="14" height="14" class="on"/><use href="#star" x="18" width="14" height="14" class="on"/><use href="#star" x="36" width="14" height="14" class="on"/><use href="#star" x="54" width="14" height="14" class="on"/><use href="#star" x="72" width="14" height="14" class="off"/></svg></li>
      <li>Average Personality<svg width="86" height="14" viewBox="0 0 86 14"><use href="#star" x="0" width="14" height="14" class="on"/><use href="#star" x="18" width="14" height="14" class="on"/><use href="#star" x="36" width="14" height="14" class="on"/><use href="#star" x="54" width="14" height="14" class="off"/><use href="#star" x="72" width="14" height="14" class="off"/></svg></li>
      <li>Works Crazy Hard<svg width="86" height="14" viewBox="0 0 86 14"><use href="#star" x="0" width="14" height="14" class="on"/><use href="#star" x="18" width="14" height="14" class="on"/><use href="#star" x="36" width="14" height="14" class="on"/><use href="#star" x="54" width="14" height="14" class="on"/><use href="#star" x="72" width="14" height="14" class="on"/></svg></li>
    </ul>
    <a class="btn dark view-details">View Details</a>
  </article>
  <article class="rank-card rc4">
    <div class="portrait-frame small"><div class="portrait small" role="img" aria-label="Portrait photo of Sam Turner" style="position:relative;width:100%;height:100%"><div class="rank-badge"></div><span class="rank-num">4<sup>st</sup></span><span class="rank-tag">BEST</span></div></div>
    <h2 class="card-name">Sam Turner</h2><p class="card-count">Number Of Reviews : 45</p>
    <ul class="traits small">
      <li>Smart<svg width="86" height="14" viewBox="0 0 86 14"><use href="#star" x="0" width="14" height="14" class="on"/><use href="#star" x="18" width="14" height="14" class="on"/><use href="#star" x="36" width="14" height="14" class="on"/><use href="#star" x="54" width="14" height="14" class="on"/><use href="#star" x="72" width="14" height="14" class="off"/></svg></li>
      <li>Average Personality<svg width="86" height="14" viewBox="0 0 86 14"><use href="#star" x="0" width="14" height="14" class="on"/><use href="#star" x="18" width="14" height="14" class="on"/><use href="#star" x="36" width="14" height="14" class="on"/><use href="#star" x="54" width="14" height="14" class="off"/><use href="#star" x="72" width="14" height="14" class="off"/></svg></li>
      <li>Works Crazy Hard<svg width="86" height="14" viewBox="0 0 86 14"><use href="#star" x="0" width="14" height="14" class="on"/><use href="#star" x="18" width="14" height="14" class="on"/><use href="#star" x="36" width="14" height="14" class="on"/><use href="#star" x="54" width="14" height="14" class="on"/><use href="#star" x="72" width="14" height="14" class="on"/></svg></li>
    </ul>
    <a class="btn dark view-details">View Details</a>
  </article>
</section>

<footer class="site-footer">Copyright © 2016 Prime Desk Rankings. All Rights Reserved.</footer>
</body>
</html>
```